buchhaltungs und lohnflyer
Zielgruppe
selbständige, freiberuflyer, freelancer, kleinbetrieb, mittelständige firma
Aufgabenstellung
dieser txt von diesem beispielflyer möchte ich gerne übernehmen. das layout soll von ihnen kommen
siehe anhang
evtl. könnte auch auf der letzten seite noch auf unser empfehlungspaket hingewiesen werden, wenn mandanten und weiterempfehlen und der neue mandant wird kunde! hier bedanken wir uns gerne mit eine kleinen Prämie! Der flyer sollte din a lang sein und hochkannt, wenn möglich!evtl muss es auch kein klappflyer sein und kann nur auf normal so a lang Flyer sein! Aber ich glaube dafür ist der txt zu viel ! Es soll als Werbung verwendet werden zum verteilen und evtl prospekteinlage ! Ist generell ein werbeflyer

```html
<!DOCTYPE html>
<html lang="de">
<head>
<meta charset="utf-8">
<title>Zahlwerk GmbH – Flyer Finanz- und Lohnbuchhaltung</title>
<link rel="stylesheet" href="https://fonts.googleapis.com/css2?family=Quicksand:wght@400;500;600;700&family=Roboto+Condensed:wght@400;700&display=swap">
<style>
  :root{
    --blue:#5f7dc1;
    --blue-soft:rgba(120,146,210,.82);
    --mist:#b5c2d4;
    --white:#ffffff;
    --ink:#6b6f78;
    --stage:#8c8c8c;
  }
  *{margin:0;padding:0;box-sizing:border-box}
  html,body{width:1198px;height:1200px;overflow:hidden;background:var(--stage)}
  body{position:relative;font-family:"Quicksand",sans-serif;color:var(--white)}
  .panel{position:absolute;left:334px;width:530px;overflow:hidden}
  .panel--outside{top:41px;height:528px;background:var(--blue)}
  .panel--inside{top:611px;height:532px;background:var(--white)}
  .abs{position:absolute}
  .block{position:absolute}

  /* brand */
  .brand{position:absolute;top:32px;width:266px;text-align:center}
  .brand__square{display:block;width:17px;height:17px;margin:0 auto 8px;background:currentColor}
  .brand__name{font-size:15px;font-weight:500;letter-spacing:1.5px}
  .brand--light{left:0;color:var(--white)}
  .brand--dark{left:266px;color:var(--blue)}

  /* outside panel */
  .referral{left:0;top:110px;width:266px;height:173px;background:var(--mist)}
  .referral__title{left:27px;top:136px;font-size:15px;font-weight:500;letter-spacing:.2px}
  .referral__text{left:111px;top:163px;width:146px;font-size:9.3px;line-height:14.2px;font-weight:500;color:var(--blue)}
  .photo{background:linear-gradient(160deg,#f2f3f6 0%,#d8dbe1 45%,#c2b6a4 85%,#a89880 100%)}
  .photo--files{left:266px;top:110px;width:262px;height:173px}
  .badge{position:absolute;border-radius:50%;display:flex;flex-direction:column;align-items:center;justify-content:center;font-family:"Roboto Condensed",sans-serif;text-align:center;line-height:1}
  .badge__inner{transform:rotate(-14deg)}
  .badge__amount{font-size:20px;font-weight:700;display:block;margin-bottom:2px}
  .badge__label{font-size:10px;display:block;line-height:11px}
  .badge--dark{left:20px;top:174px;width:80px;height:80px;background:var(--blue);border:2px solid var(--white);color:var(--mist)}
  .badge--light{left:402px;top:246px;width:83px;height:83px;background:var(--mist);border:3px solid var(--white);color:var(--white)}
  .badge--light .badge__inner{transform:rotate(10deg)}
  .badge--light .badge__label{color:var(--blue)}
  .service-title{left:285px;top:366px;font-size:16px;font-weight:500;line-height:19px;letter-spacing:.2px}
  .service-sub{left:285px;top:420px;font-size:10.5px;line-height:14px;font-weight:500}
  .contact{left:51px;top:403px;font-size:9.3px;line-height:14.2px}
  .contact__name{font-weight:600;margin-bottom:4px}
  .contact__row{position:relative}
  .contact__icon{position:absolute;left:-17px;top:2px;width:10px;height:10px;fill:var(--white)}

  /* inside panel */
  .partner{left:0;top:0;width:266px;height:112px;background:var(--blue)}
  .partner__title{left:18px;top:41px;font-size:15px;font-weight:500;color:var(--mist)}
  .partner__text{left:18px;top:66px;font-size:12px;line-height:15px;font-weight:500}
  .photo--handover{left:266px;top:0;width:266px;height:241px;background:linear-gradient(180deg,#d9dde6 0%,#eef0f3 55%,#c9a88f 75%,#e6e8ec 100%)}
  .quote{left:266px;top:0;width:266px;height:112px;background:var(--blue-soft)}
  .quote__mark{left:296px;top:14px;font-size:30px;font-weight:700;line-height:1}
  .quote__text{left:296px;top:40px;width:210px;font-size:12px;line-height:15px;font-weight:500}
  .section-title{left:22px;top:145px;font-size:17.5px;font-weight:600;color:var(--blue);letter-spacing:.3px}
  .section-lead{left:22px;top:180px;font-size:12.4px;line-height:15px;color:var(--mist);font-weight:500}
  .list-title{font-size:10px;font-weight:600;color:var(--blue);letter-spacing:.2px}
  .list{list-style:none;font-size:8.7px;line-height:14.3px;color:var(--ink);margin-top:2px}
  .list li::before{content:"+";color:var(--mist);font-weight:700;margin-right:2px}
  .list--finance{left:22px;top:218px}
  .list--payroll{left:22px;top:334px}
  .expert-title{left:291px;top:264px}
  .expert{left:304px;top:286px;width:208px;list-style:none;font-size:8.7px;line-height:12.4px;color:var(--ink);text-align:justify}
  .expert li{position:relative;margin-bottom:9px}
  .expert__star{position:absolute;left:-12px;top:1px;width:9px;height:9px;fill:var(--mist)}
  .audience{left:0;top:440px;width:266px;height:92px;background:var(--mist)}
  .audience__title{left:18px;top:454px;font-size:15px;font-weight:500}
  .audience__text{left:18px;top:482px;font-size:12px;line-height:15px;color:var(--blue);font-weight:500}
  .values{left:266px;top:440px;width:266px;height:92px;background:var(--blue)}
  .values__list{left:290px;top:470px;width:220px;list-style:none;display:grid;grid-template-columns:110px 110px;grid-auto-flow:column;grid-template-rows:repeat(3,14px);font-size:12px;font-weight:500}
  .values__list li{display:flex;align-items:center;gap:4px}
  .tick{width:9px;height:9px;stroke:var(--mist);stroke-width:2;fill:none}
</style>
</head>
<body>

<section class="panel panel--outside">
  <div class="brand brand--light"><span class="brand__square"></span><span class="brand__name">ZAHLWERK GMBH</span></div>
  <div class="brand brand--dark"><span class="brand__square"></span><span class="brand__name">ZAHLWERK GMBH</span></div>

  <div class="block referral"></div>
  <h2 class="abs referral__title">UNSER EMPFEHLUNGSPAKET</h2>
  <div class="badge badge--dark"><div class="badge__inner"><span class="badge__amount">XX €</span><span class="badge__label">FÜR IHRE<br>EMPFEHLUNG</span></div></div>
  <p class="abs referral__text">Wenn Sie als Mandant uns weiterempfehlen und der neue Mandant wird Kunde bei uns, bedanken wir uns gerne mit einer kleinen Prämie in Höhe von XX €!</p>

  <div class="block photo photo--files" role="img" aria-label="Foto: aufgeschlagene Aktenordner im Regal"></div>
  <div class="badge badge--light"><div class="badge__inner"><span class="badge__amount">XX €*</span><span class="badge__label">FÜR IHRE<br>EMPFEHLUNG</span></div></div>

  <h1 class="abs service-title">FINANZBUCHHALTUNG UND<br>LOHNBUCHHALTUNG</h1>
  <p class="abs service-sub">Für Selbständige, Freiberufler, Freelancer,<br>Klein- und mittelständische Unternehmen</p>

  <address class="abs contact" style="font-style:normal">
    <div class="contact__name">Zahlwerk GmbH</div>
    <div class="contact__row"><svg class="contact__icon" viewBox="0 0 10 10"><path d="M5 0a3.5 3.5 0 0 0-3.5 3.5C1.5 6 5 10 5 10s3.5-4 3.5-6.5A3.5 3.5 0 0 0 5 0zm0 5a1.4 1.4 0 1 1 0-2.8A1.4 1.4 0 0 1 5 5z"/></svg>Lindenweg 12</div>
    <div class="contact__row">70199 Talheim</div>
    <div class="contact__row"><svg class="contact__icon" viewBox="0 0 10 10"><rect x="2.5" y="0" width="5" height="10" rx="1"/></svg>0711 / 000 111 20</div>
    <div class="contact__row"><svg class="contact__icon" viewBox="0 0 10 10"><rect x="2" y="0" width="6" height="4"/><rect x="0" y="4" width="10" height="4" rx="1"/><rect x="2" y="8" width="6" height="2"/></svg>0711 / 000 111 29</div>
    <div class="contact__row"><svg class="contact__icon" viewBox="0 0 10 10"><path d="M0 2h10v6H0z"/><path d="M0 2l5 4 5-4" stroke="#5f7dc1" stroke-width="1" fill="none"/></svg>info@zahlwerk-buero.de</div>
    <div class="contact__row"><svg class="contact__icon" viewBox="0 0 10 10"><circle cx="5" cy="5" r="5"/><path d="M0 5h10M5 0v10M1.5 2.5h7M1.5 7.5h7" stroke="#5f7dc1" stroke-width=".8" fill="none"/></svg>www.zahlwerk-buero.de</div>
  </address>
</section>

<section class="panel panel--inside">
  <div class="block partner"></div>
  <h2 class="abs partner__title">WIR SIND IHR PARTNER!</h2>
  <p class="abs partner__text">Kundenfreundlich in<br>Leistung - Preis - Service</p>

  <div class="block photo photo--handover" role="img" aria-label="Foto: zwei Hände übergeben einen Aktenordner"></div>
  <div class="block quote"></div>
  <span class="abs quote__mark">”</span>
  <p class="abs quote__text">Wir geben Ihnen die verlorene Zeit am Schreibtisch zurück. Konzentrieren Sie sich auf Ihr Kerngeschäft!</p>

  <h2 class="abs section-title">UNSER SERVICE</h2>
  <p class="abs section-lead">So profitieren Sie von unserer<br>modernen Datenverabeitung</p>

  <div class="abs list--finance">
    <h3 class="list-title">FINANZBUCHHALTUNG</h3>
    <ul class="list">
      <li>Sortieren und Kontieren der Belege</li>
      <li>Buchen der laufenden Geschäftsvorfälle</li>
      <li>Debitoren- und Kreditorenüberwachung</li>
      <li>Betriebswirtschaftliche Beratung</li>
      <li>Verwaltung des kaufmännischen Mahnwesens</li>
      <li>weitere kaufmännische Dienstleistungen auf Anfrage</li>
    </ul>
  </div>
  <div class="abs list--payroll">
    <h3 class="list-title">LOHNBUCHHALTUNG</h3>
    <ul class="list">
      <li>Laufende Lohn-/Gehaltsabrechnung</li>
      <li>Fertigen der Lohnsteueranmeldung</li>
      <li>Beitragsnachweise an die Krankenkassen</li>
      <li>An- und Abmeldungen bei den Krankenkassen</li>
      <li>Meldungen an die Berufsgenossenschaft</li>
    </ul>
  </div>

  <h3 class="abs list-title expert-title">ALS EXPERTEN ...</h3>
  <ul class="abs expert">
    <li><svg class="expert__star" viewBox="0 0 10 10"><path d="M5 0l1.5 3.3 3.5.4-2.6 2.4.7 3.5L5 7.9 1.9 9.6l.7-3.5L0 3.7l3.5-.4z"/></svg>.. sind wir spezialisiert auf das Buchen laufender Geschäftsvorfälle, Ihrer Finanzbuchhaltung und auf die Erstellung der laufenden Lohn- und Gehaltsab­rechnung.</li>
    <li><svg class="expert__star" viewBox="0 0 10 10"><path d="M5 0l1.5 3.3 3.5.4-2.6 2.4.7 3.5L5 7.9 1.9 9.6l.7-3.5L0 3.7l3.5-.4z"/></svg>Unser Fachwissen zeichnet uns aus und führt zu optimalen Resultaten, insbesondere im Steuerrecht bilden wir uns ständig weiter.</li>
    <li><svg class="expert__star" viewBox="0 0 10 10"><path d="M5 0l1.5 3.3 3.5.4-2.6 2.4.7 3.5L5 7.9 1.9 9.6l.7-3.5L0 3.7l3.5-.4z"/></svg>Die Kosten für diese Leistungen können Sie genau kalkulieren, ohne Ihren Betrieb mit zusätzlichen Personalkosten zu belasten</li>
  </ul>

  <div class="block audience"></div>
  <h2 class="abs audience__title">IHR PARTNER FÜR ...</h2>
  <p class="abs audience__text">... Selbständige, Freiberufler, Freelancer,<br>Klein- und mittelständische Unternehmen</p>

  <div class="block values"></div>
  <ul class="abs values__list">
    <li><svg class="tick" viewBox="0 0 10 10"><path d="M1 5l3 3 5-7"/></svg>fachkundig</li>
    <li><svg class="tick" viewBox="0 0 10 10"><path d="M1 5l3 3 5-7"/></svg>freundlich</li>
    <li><svg class="tick" viewBox="0 0 10 10"><path d="M1 5l3 3 5-7"/></svg>zuverlässig</li>
    <li><svg class="tick" viewBox="0 0 10 10"><path d="M1 5l3 3 5-7"/></svg>preiswert</li>
    <li><svg class="tick" viewBox="0 0 10 10"><path d="M1 5l3 3 5-7"/></svg>flexibel</li>
    <li><svg class="tick" viewBox="0 0 10 10"><path d="M1 5l3 3 5-7"/></svg>qualifiziert</li>
  </ul>
</section>

</body>
</html>
```